Coastal Mulchworks Inc

Industry/Entity Type

Forestry

Contact Information for Business Card

Company name: Coastal Mulchworks INC, Contact Info: Rulemo Vantaro, Phone # 843 555 0187, Addres: 248 Whitlow Ferry Rd, Ashdale SC 29540, Email: coastalmulch@example.test

```html
<!DOCTYPE html>
<html lang="en">
<head>
<meta charset="utf-8">
<title>Coastal Mulchworks INC — Business Card</title>
<link href="https://fonts.googleapis.com/css2?family=Ubuntu:wght@400;500;700&display=swap" rel="stylesheet">
<style>
  :root {
    --page-bg: #ececec;
    --card-bg: #f6f7f7;
    --gold: #c09a5b;
    --ink: #1d1d1d;
    --straw-a: #b98a5f;
    --straw-b: #8f6646;
    --straw-c: #d2ab84;
  }
  * { margin: 0; padding: 0; box-sizing: border-box; }
  html, body { width: 826px; height: 1200px; overflow: hidden; }
  body {
    background: var(--page-bg);
    font-family: "Ubuntu", Arial, sans-serif;
    position: relative;
  }
  .card {
    position: absolute;
    left: 96px;
    width: 637px;
    height: 362px;
    background: var(--card-bg);
    overflow: hidden;
  }
  .card--front { top: 128px; }
  .card--back { top: 644px; }

  .straw-fill {
    background: linear-gradient(135deg, var(--straw-c) 0%, var(--straw-a) 45%, var(--straw-b) 100%);
  }
  .front__photo {
    position: absolute;
    left: 55px; top: 59px;
    width: 230px; height: 219px;
  }
  .front__company {
    position: absolute;
    left: 55px; top: 284px;
    width: 230px;
    text-align: center;
    color: var(--gold);
    font-weight: 700;
    font-size: 20px;
    white-space: nowrap;
  }
  .front__person {
    position: absolute;
    left: 357px; top: 92px;
  }
  .person__name {
    color: var(--gold);
    font-size: 22px;
    font-weight: 400;
    line-height: 1.2;
  }
  .person__name strong { font-weight: 700; }
  .person__title {
    color: var(--ink);
    font-size: 14px;
    margin-top: 1px;
  }
  .contact-list {
    position: absolute;
    left: 332px; top: 155px;
    list-style: none;
    color: var(--ink);
    font-size: 15px;
    line-height: 23.5px;
  }
  .contact-list li { display: flex; align-items: flex-start; }
  .contact-list .icon {
    width: 14px; height: 14px;
    margin: 5px 11px 0 0;
    flex: none;
  }
  .contact-list .no-icon { margin-left: 25px; }

  .back__band {
    position: absolute; left: 0; width: 100%;
  }
  .back__band--top { top: 0; height: 126px; }
  .back__band--bottom { top: 237px; height: 125px; }
  .back__company {
    position: absolute;
    left: 0; top: 126px;
    width: 100%; height: 111px;
    display: flex; align-items: center; justify-content: center;
    color: var(--gold);
    font-weight: 700;
    font-size: 30px;
  }
</style>
</head>
<body>
  <section class="card card--front">
    <div class="front__photo straw-fill" role="img" aria-label="Close-up photo of dry pine straw needles"></div>
    <div class="front__company">Coastal Mulchworks INC</div>

    <div class="front__person">
      <div class="person__name"><strong>Rulemo</strong> Vantaro</div>
      <div class="person__title">CEO</div>
    </div>

    <ul class="contact-list">
      <li>
        <svg class="icon" viewBox="0 0 14 14" aria-hidden="true">
          <circle cx="7" cy="7" r="6.3" fill="none" stroke="var(--gold)" stroke-width="1"/>
          <path d="M4.6 4.2c.4-.4.8-.4 1 0l.6 1c.2.3.1.6-.2.8l-.3.2c.3.8.9 1.5 1.8 1.9l.3-.3c.2-.3.5-.3.8-.1l1 .6c.4.2.4.6 0 1l-.5.4c-2.3.3-5-2.4-4.8-4.9z" fill="var(--gold)"/>
        </svg>
        843 555 0187
      </li>
      <li>
        <svg class="icon" viewBox="0 0 14 14" aria-hidden="true">
          <circle cx="7" cy="7" r="6.3" fill="none" stroke="var(--gold)" stroke-width="1"/>
          <rect x="3.8" y="4.8" width="6.4" height="4.4" rx="0.6" fill="var(--gold)"/>
          <path d="M3.9 5.1 7 7.2l3.1-2.1" fill="none" stroke="var(--card-bg)" stroke-width="0.7"/>
        </svg>
        coastalmulch@example.test
      </li>
      <li>
        <svg class="icon" viewBox="0 0 14 14" aria-hidden="true">
          <circle cx="7" cy="7" r="6.3" fill="none" stroke="var(--gold)" stroke-width="1"/>
          <path d="M7 3.3a2.5 2.5 0 0 1 2.5 2.5c0 1.8-2.5 4.6-2.5 4.6S4.5 7.6 4.5 5.8A2.5 2.5 0 0 1 7 3.3z" fill="none" stroke="var(--gold)" stroke-width="1"/>
          <circle cx="7" cy="5.8" r="0.9" fill="var(--gold)"/>
        </svg>
        248 Whitlow Ferry Rd
      </li>
      <li><span class="no-icon">Ashdale SC 29540</span></li>
    </ul>
  </section>

  <section class="card card--back">
    <div class="back__band back__band--top straw-fill" role="img" aria-label="Photo band of dry pine straw needles"></div>
    <div class="back__company">Coastal Mulchworks INC</div>
    <div class="back__band back__band--bottom straw-fill" role="img" aria-label="Photo band of dry pine straw needles"></div>
  </section>
</body>
</html>
```